Tall Harbor Business Card

We are a Video Production and Video Equipment Rental company specialising in the supply of state of the art Video Technology and Services for the Live Entertainment, Television and Corporate Business Theatre markets. (in Sydney, Australia) www.tallharbor-media.example

Industry/Entity Type

Business

Contact Information for Business Card

name, position, email, website, address, logo
Example attached of the information we need - doesn't necessarily have to look the same

Font styles to use
Other font styles liked:
• Tall Harbor logo font is GOTHAM

Colors
ea1f27

Requirements
Nice to have
• either matt black or shiny black cards -
raised logo

```html
<!DOCTYPE html>
<html lang="en">
<head>
<meta charset="utf-8">
<title>Tall Harbor Business Card</title>
<link rel="stylesheet" href="https://fonts.googleapis.com/css2?family=Arimo:wght@400&family=Montserrat:wght@500&display=swap">
<style>
  :root {
    --brand-red: #ea1f27;
    --card-black: #000000;
    --accent-teal: #00627f;
    --paper: #ffffff;
    --ink: #000000;
  }
  html, body {
    margin: 0;
    padding: 0;
    width: 1200px;
    height: 720px;
    overflow: hidden;
    background: var(--paper);
  }
  .business-card {
    position: relative;
    width: 1200px;
    height: 720px;
    background: var(--paper);
    font-family: "Arimo", Arial, sans-serif;
    overflow: hidden;
  }
  .brand-panel {
    position: absolute;
    left: 0;
    top: 0;
    width: 520px;
    height: 720px;
    background: var(--card-black);
  }
  .accent-band {
    position: absolute;
    left: 520px;
    top: 0;
    width: 70px;
    height: 720px;
    background: linear-gradient(180deg, var(--brand-red) 0%, var(--brand-red) 45%, var(--accent-teal) 100%);
  }

  .brand-name {
    position: absolute;
    left: 257px;
    top: 340px;
    transform: translate(-50%, -50%);
    margin: 0;
    font-family: "Montserrat", Arial, sans-serif;
    font-weight: 500;
    font-size: 46px;
    letter-spacing: 1px;
    color: var(--paper);
    white-space: nowrap;
  }

  .person {
    position: absolute;
    right: 14px;
    top: 14px;
    text-align: right;
  }
  .person-name {
    margin: 0;
    font-size: 56px;
    font-weight: 400;
    line-height: 1;
    color: var(--brand-red);
  }
  .person-role {
    margin: 12px 0 0;
    font-size: 35px;
    line-height: 1;
    color: var(--accent-teal);
  }

  .contact {
    position: absolute;
    left: 659px;
    width: 486px;
    top: 280px;
    text-align: center;
    color: var(--ink);
  }
  .contact-email {
    display: block;
    font-size: 33px;
    line-height: 40px;
    white-space: nowrap;
  }
  .contact-rule {
    height: 6px;
    background: var(--ink);
    margin: 8px 0 10px;
  }
  .contact-web {
    display: block;
    font-size: 25px;
    line-height: 30px;
    white-space: nowrap;
  }

  .address {
    position: absolute;
    right: 12px;
    top: 606px;
    margin: 0;
    text-align: right;
    font-style: normal;
    color: var(--ink);
    line-height: 1;
  }
  .address-street { display: block; font-size: 37px; }
  .address-city { display: block; font-size: 27px; margin-top: 4px; }
  .address-country { display: block; font-size: 35px; margin-top: 2px; }
</style>
</head>
<body>
  <main class="business-card">
    <div class="brand-panel"></div>
    <div class="accent-band" role="img" aria-label="Decorative sweeping bands in red and teal"></div>

    <p class="brand-name">TALL HARBOR</p>

    <header class="person">
      <h1 class="person-name">LUCA MORETTI</h1>
      <p class="person-role">Managing director</p>
    </header>

    <div class="contact">
      <span class="contact-email">LUCA@TALLHARBOR.EXAMPLE</span>
      <div class="contact-rule"></div>
      <span class="contact-web">WWW.TALLHARBOR-MEDIA.EXAMPLE</span>
    </div>

    <address class="address">
      <span class="address-street">18 KEEL STREET</span>
      <span class="address-city">MARRICK NSW 2090</span>
      <span class="address-country">AUSTRALIA</span>
    </address>
  </main>
</body>
</html>
```